food delivery web site design

Currently we have a smartphone app (ios/android) that is being used by our clients to make orders to about 30 different restaurants.

We would like to extent this and have also a website that is able to mimic the same functionalities:
- register
- show restaurants based on the selected address
- make order to an restaurant
- being able to process orders for other registered users (please read the attached doc for complete info on this)

Take a look at the attached doc for more info.

Android

```html
<!DOCTYPE html>
<html lang="ro">
<head>
<meta charset="utf-8">
<title>Gustara – Confirmare cod</title>
<link href="https://fonts.googleapis.com/css2?family=Bebas+Neue&family=Oswald:wght@400&family=Open+Sans:wght@400&family=Pacifico&display=swap" rel="stylesheet">
<style>
  :root {
    --red: #9b1608;
    --red-dark: #7a1005;
    --tab: #2a2424;
    --pattern-light: #f1f1f1;
    --footer-bg: #222222;
    --footer-pattern: #2c2c2c;
    --title-grey: #c8c8c8;
    --label-grey: #666666;
    --rule: #d4d4d4;
    --button-grey: #666666;
    --phone-yellow: #f7d46a;
    --white: #ffffff;
  }
  * { margin: 0; padding: 0; box-sizing: border-box; }
  html, body { width: 1200px; height: 831px; overflow: hidden; background: var(--white); }
  .page { position: relative; width: 1200px; height: 831px; }

  .header-pattern {
    position: absolute; left: 0; top: 0; width: 1200px; height: 50px;
    background: linear-gradient(180deg, var(--pattern-light), #e6e6e6);
  }
  .header-band {
    position: absolute; left: 0; top: 50px; width: 1200px; height: 53px;
    background: var(--red);
    border-top: 2px solid var(--red-dark);
    border-bottom: 2px solid var(--red-dark);
  }
  .band-line { position: absolute; top: 27px; height: 0; border-top: 1px solid rgba(255,255,255,0.6); border-bottom: 1px solid rgba(255,255,255,0.6); padding-top: 2px; }
  .band-line--left { left: 297px; width: 36px; }
  .band-line--right { left: 1063px; width: 137px; }
  .band-dots { position: absolute; left: 609px; top: 27px; width: 277px; border-top: 1px dotted rgba(255,255,255,0.7); border-bottom: 1px dotted rgba(255,255,255,0.7); height: 4px; }

  .call-us {
    position: absolute; left: 350px; top: 62px;
    font-family: 'Bebas Neue', sans-serif; font-size: 29px; color: var(--white); letter-spacing: 0.2px;
    display: flex; align-items: center; gap: 6px;
  }
  .call-us__phone { color: var(--phone-yellow); display: flex; align-items: center; gap: 3px; }

  .account-links { position: absolute; left: 906px; top: 68px; display: flex; gap: 24px; }
  .account-link {
    font-family: 'Oswald', sans-serif; font-size: 14px; color: var(--white); text-decoration: none;
    display: flex; align-items: center; gap: 6px; text-transform: uppercase;
  }

  .brand-tab { position: absolute; left: 138px; top: 0; width: 160px; height: 160px; }
  .brand-name {
    position: absolute; left: 163px; top: 23px; width: 110px; height: 110px;
    display: flex; align-items: center; justify-content: center;
    font-family: 'Oswald', sans-serif; font-size: 22px; color: var(--red);
  }

  .content { position: absolute; left: 138px; top: 230px; width: 923px; }
  .page-title {
    font-family: 'Bebas Neue', sans-serif; font-weight: 400; font-size: 54px; color: var(--title-grey);
    line-height: 1; padding-left: 2px; padding-bottom: 9px;
    border-bottom: 1px solid var(--rule);
  }
  .code-label {
    margin-top: 40px;
    font-family: 'Bebas Neue', sans-serif; font-size: 21px; color: var(--label-grey); letter-spacing: 0.3px;
    display: block;
  }
  .code-input {
    display: block; margin-top: 10px; width: 249px; height: 42px;
    border: 1px solid #cfcfcf; background: var(--white);
  }
  .actions { margin-top: 35px; display: flex; gap: 19px; }
  .btn {
    height: 42px; border: none; color: var(--white);
    font-family: 'Oswald', sans-serif; font-size: 18px; text-transform: uppercase;
    padding: 0 15px;
  }
  .btn--secondary { width: 135px; background: var(--button-grey); }
  .btn--primary { width: 105px; background: var(--red); }

  .site-footer { position: absolute; left: 0; top: 775px; width: 1200px; height: 56px; background: var(--footer-bg); }
  .footer-pattern { position: absolute; inset: 0; background: linear-gradient(90deg, var(--footer-pattern), var(--footer-bg), var(--footer-pattern)); }
  .footer-nav { position: absolute; left: 138px; top: 20px; display: flex; font-family: 'Open Sans', sans-serif; font-size: 12.5px; }
  .footer-nav a { color: var(--white); text-decoration: none; padding: 0 9px; border-left: 1px solid #555; line-height: 1.2; }
  .footer-nav a:first-child { padding-left: 0; border-left: none; }
  .copyright { position: absolute; right: 139px; top: 20px; font-family: 'Open Sans', sans-serif; font-size: 12.5px; color: var(--white); line-height: 1.2; }
</style>
</head>
<body>
<div class="page">
  <div class="header-pattern" role="img" aria-label="Light pattern of hand-drawn food doodles"></div>

  <header class="header-band">
    <span class="band-line band-line--left"></span>
    <span class="band-dots"></span>
    <span class="band-line band-line--right"></span>
  </header>

  <div class="call-us">
    <span>Sună-ne la</span>
    <span class="call-us__phone">
      <svg width="16" height="20" viewBox="0 0 16 20" aria-hidden="true"><path d="M4 1 L7 5 L5 8 Q7 13 10 15 L13 13 L15 17 L12 19 Q4 16 2 5 Z" fill="none" stroke="var(--phone-yellow)" stroke-width="2" stroke-linejoin="round"/></svg>
      0700 555 123
    </span>
  </div>

  <nav class="account-links">
    <a class="account-link" href="#">
      <svg width="14" height="13" viewBox="0 0 14 13" aria-hidden="true"><path d="M1 12 V8 Q1 5 5 5 H9 V1 L14 6 L9 11 V8 H5 Q4 8 4 12 Z" fill="var(--white)"/></svg>
      Login
    </a>
    <a class="account-link" href="#">
      <svg width="16" height="12" viewBox="0 0 16 12" aria-hidden="true"><circle cx="6" cy="4" r="3" fill="var(--white)"/><path d="M0 12 Q0 7 6 7 Q12 7 12 12 Z" fill="var(--white)"/><path d="M13 1 V6 M10.5 3.5 H15.5" stroke="var(--white)" stroke-width="1.6"/></svg>
      Sign in
    </a>
  </nav>

  <svg class="brand-tab" viewBox="0 0 160 160" aria-hidden="true">
    <path d="M0 0 H160 V130 L138 152 H22 L0 130 Z" fill="var(--tab)"/>
    <path d="M6 0 V127 L25 146 H135 L154 127 V0" fill="none" stroke="#8a8080" stroke-width="1"/>
    <circle cx="80" cy="78" r="56" fill="var(--white)"/>
    <circle cx="80" cy="82" r="46" fill="#ececec"/>
  </svg>
  <div class="brand-name">Gustara</div>

  <main class="content">
    <h1 class="page-title">Confirmare cod</h1>
    <label class="code-label" for="sms-code">Introdu codul din 4 litere primit prin SMS</label>
    <input class="code-input" id="sms-code" type="text" maxlength="4">
    <div class="actions">
      <button class="btn btn--secondary" type="button">Retrimite cod</button>
      <button class="btn btn--primary" type="submit">Confirmă</button>
    </div>
  </main>

  <footer class="site-footer">
    <div class="footer-pattern" role="img" aria-label="Dark pattern of hand-drawn food doodles"></div>
    <nav class="footer-nav">
      <a href="#">Contactează-ne</a>
      <a href="#">Despre noi</a>
      <a href="#">Partenerii noștri</a>
      <a href="#">FAQ</a>
      <a href="#">Devino partener</a>
    </nav>
    <p class="copyright">Copyright © 2013 gustara.ro. Toate drepturile rezervate.</p>
  </footer>
</div>
</body>
</html>
```